Velmar Cyber Security (Consultants)

We need a webdesign for a new website www.velmarcybersecurity.example.

A draft version of the website is online. You can also look at our linkedIn company page: http://www.linkedin.example/company/7412096

This is what we do:
We defend our cybersociety against the growing number of cyber threats in order to allow our society to prosper and evolve more safely into the digital age. We seek to protect 4 key pillars of our society: critical (industrial) infrastructures, medical systems, our intellectual property, and financial systems.

Velmar is specialised in IT & information security consultancy and positions itself as an independent partner. Our employees possess a unique mix of technical hands-on engineering and consulting skills. We invest time and resources to learn about existing open-source and commercial technologies in order to give better advice.

We are no-nonsense, practical and to the point.

We advise and guide organisations with the strategy, definition and technical implementation of security projects. We take ownership in aligning the existing business, operational and technical context.

Some requirements:
- Ideally you deliver a fully coded and designed static website. I am hosting the website on www.hostbay.example; you can use the technologies that are supported there.
- My existing company colors and logos need to be preserved (see existing websites & linkedIn page)
- I would like a white background (is the best fit for my existing logo's, and easiest to maintain afterwards)
Some examples, but please feel free: http://www.stoneward.example/ http://www.quevix.example/ )
- I will use twitter as a way to update my website with relevant news ; So I want the twitterfeed integrated in the website, certianly on the homepage; if possible on all pages. (www.twitter.example/velmarsecurity)
- I am using my linkedIn company page; I want at least the "Follow" company button to be integrated in the website. (http://www.linkedin.example/company/velmar-cybersecurity-consultants/)
- it should be possible for me to do some minor updates to the site.
- I need several nice banners that I could also re-use at my linkedIn webpage (linkedIn requires 646 x 220 pixels or larger banners)

- As I see it now, the website should have a Home page that immediately displays the core services we offer. A basic Jobs page. an about and contact page where people can leave their details behind.
- Optional: An industries tab where there are sub-sites possible
Updates

This project has just been garantueed! First and second place get a nice payment. Please send you designs. 

I need
- A ready to deploy basic HTML webpage
- 4 pages: Home, Services, Careers, About/contact
- Some nice banners designed on my mission statement (in the brief)

Thanks

Reason: We would like to receive some more designs from other designers.

Target Market(s)

From medium sized KMO's, to mainly big enterprises.
My focusses is on strategic consulting, So managers, decision takers & business people
The site should also attrack consultants that have technical skills and managerial skills...

Industry/Entity Type

Financial

Requirements
Must have
• - My existing company colors and logos need to be preserved (see existing websites & linkedIn page)
- I would like a clean, professional site, with a white background
- As I see it now, the website should have a Home page that immediately displays the core services we offer. A basic careers page. an about and contact page where people can leave their details behind.
Nice to have
• - it should be possible for me to do some minor updates to the site.

```html
<!DOCTYPE html>
<html lang="en">
<head>
<meta charset="utf-8">
<title>Velmar Cyber Security – Home</title>
<link rel="stylesheet" href="https://fonts.googleapis.com/css2?family=Oswald:wght@400;500;600&family=Open+Sans:wght@400;600;700&display=swap">
<style>
:root{
  --red:#d3122a;
  --red-dark:#8f0616;
  --red-mid:#b80c22;
  --ink:#333333;
  --muted:#555555;
  --grey-band:#e4e4e4;
  --grey-line:#cfcfcf;
  --footer:#2b2b2b;
  --white:#ffffff;
  --screen-a:#0d2c4a;
  --screen-b:#3e78a8;
}
*{box-sizing:border-box;margin:0;padding:0}
html,body{width:898px;height:1200px;overflow:hidden}
body{background:var(--white);font-family:"Open Sans",Arial,sans-serif;color:var(--ink);position:relative}

/* header */
.site-header{height:62px;background:linear-gradient(#f4f4f4,#dcdcdc);position:relative}
.brand{position:absolute;left:40px;top:0;height:62px;padding:0 22px;background:var(--white);display:flex;align-items:center;gap:10px;box-shadow:0 2px 6px rgba(0,0,0,.15)}
.brand-mark{width:16px;height:16px;background:var(--red)}
.brand-name{font-family:"Oswald",Arial,sans-serif;font-weight:600;font-size:30px;color:var(--red);letter-spacing:.5px}
.main-nav{position:absolute;right:40px;top:16px;display:flex;background:var(--white);border-radius:16px;padding:4px 8px;box-shadow:0 1px 4px rgba(0,0,0,.2)}
.main-nav a{font-family:"Oswald",Arial,sans-serif;font-size:12px;color:var(--ink);text-decoration:none;padding:5px 14px;border-right:1px solid var(--grey-line)}
.main-nav a:last-child{border-right:none}
.main-nav a.is-active{color:var(--red)}

/* hero */
.hero{height:418px;background:radial-gradient(ellipse at 50% 45%,var(--red) 0%,var(--red-mid) 45%,var(--red-dark) 100%);position:relative;text-align:center;color:var(--white)}
.hero-visual{position:absolute;left:250px;top:18px;width:398px;height:262px;border-radius:10px 10px 4px 4px;background:linear-gradient(160deg,var(--screen-b),var(--screen-a));box-shadow:0 10px 22px rgba(0,0,0,.35)}
.hero-arrow{position:absolute;top:170px}
.hero-arrow.prev{left:26px}
.hero-arrow.next{right:26px}
.hero-title{position:absolute;top:296px;left:0;right:0;font-family:"Oswald",Arial,sans-serif;font-weight:500;font-size:34px;line-height:42px;letter-spacing:.5px;text-shadow:0 2px 3px rgba(0,0,0,.3)}
.hero-text{position:absolute;top:338px;left:200px;right:200px;font-size:13px;font-weight:600;line-height:18px}
.btn-more{position:absolute;top:378px;left:384px;width:130px;height:32px;border-radius:16px;background:linear-gradient(#ffffff,#d9d9d9);color:var(--red);font-family:"Oswald",Arial,sans-serif;font-size:14px;line-height:32px;text-decoration:none;box-shadow:0 2px 4px rgba(0,0,0,.3)}
.hero-rule{height:10px;background:var(--grey-band)}

/* section bars */
.section-bar{background:linear-gradient(#f1f1f1,#dedede);border-bottom:1px solid var(--grey-line);height:34px;padding-left:40px;font-family:"Oswald",Arial,sans-serif;font-size:17px;color:var(--red);line-height:34px}

/* featured */
.featured{height:300px;position:relative;padding:24px 40px}
.featured-copy{width:470px}
.featured-title{font-family:"Oswald",Arial,sans-serif;font-weight:500;font-size:20px;color:var(--red);line-height:26px;margin-bottom:8px;white-space:nowrap}
.body-text{font-size:11px;line-height:16px;color:var(--muted)}
.tick-list{list-style:none;margin-top:10px}
.tick-list li{font-size:11px;color:var(--muted);line-height:20px;display:flex;align-items:center;gap:8px}
.tick-list svg{flex:none}
.featured-visual{position:absolute;left:555px;top:24px;width:250px;height:180px;border-radius:12px;background:linear-gradient(160deg,var(--screen-b),var(--screen-a));border:8px solid #222}
.btn-contact{position:absolute;left:560px;top:222px;width:240px;height:30px;background:var(--red);border-radius:4px;color:var(--white);font-family:"Oswald",Arial,sans-serif;font-size:12px;text-align:center;line-height:30px;text-decoration:none}

/* lower columns */
.columns{display:flex;height:420px}
.column{flex:1}
.column + .column{border-left:1px solid var(--grey-line)}
.column-bar{background:linear-gradient(#f1f1f1,#dedede);border-top:1px solid var(--grey-line);border-bottom:1px solid var(--grey-line);height:38px;padding-left:40px;font-family:"Oswald",Arial,sans-serif;font-size:19px;color:var(--red);line-height:38px}
.column-body{padding:18px 40px}
.update{font-size:11px;line-height:16px;color:var(--muted);margin-bottom:16px}
.update strong{color:var(--red);font-weight:700}

/* footer */
.site-footer{position:absolute;left:0;right:0;bottom:0;height:56px;background:var(--footer);border-top:4px solid var(--red);display:flex;align-items:center;justify-content:space-between;padding:0 40px}
.footer-nav a{font-family:"Oswald",Arial,sans-serif;font-size:11px;color:#cfcfcf;text-decoration:none;margin-right:22px}
.social{display:flex;gap:8px}
.social span{width:22px;height:22px;border-radius:50%;background:#4a8fc9}
</style>
</head>
<body>

<header class="site-header">
  <div class="brand"><span class="brand-mark"></span><span class="brand-name">Velmar</span></div>
  <nav class="main-nav">
    <a href="#" class="is-active">HOME</a><a href="#">ABOUT</a><a href="#">SERVICES</a><a href="#">CAREER</a><a href="#">CONTACT</a>
  </nav>
</header>

<section class="hero">
  <div class="hero-visual" role="img" aria-label="Laptop showing a cybersecurity strategy screen"></div>
  <svg class="hero-arrow prev" width="24" height="50" viewBox="0 0 24 50"><polyline points="20,4 4,25 20,46" fill="none" stroke="#ffffff" stroke-width="5" stroke-linecap="round" stroke-linejoin="round"/></svg>
  <svg class="hero-arrow next" width="24" height="50" viewBox="0 0 24 50"><polyline points="4,4 20,25 4,46" fill="none" stroke="#ffffff" stroke-width="5" stroke-linecap="round" stroke-linejoin="round"/></svg>
  <h1 class="hero-title">CYBERSECURITY STRATEGY ASSESSMENT &amp; ROADMAP</h1>
  <p class="hero-text">If your organisation is looking for real and automated security that is effective and cost-efficient our approach will interest you.</p>
  <a href="#" class="btn-more">LEARN MORE...</a>
</section>
<div class="hero-rule"></div>

<div class="section-bar">FEATURED SERVICES</div>

<section class="featured">
  <div class="featured-copy">
    <h2 class="featured-title">CYBERSECURITY STRATEGY ASSESSMENT &amp; ROADMAP</h2>
    <p class="body-text">In this management consulting solution we assist and guide the Security Officer or the general management in defining and implementing an effective cybersecurity strategy. The traditional compliance-based security is failing. If your organisation is looking for real and automated security that is effective and cost-efficient our approach will interest you.</p>
    <ul class="tick-list">
      <li><svg width="13" height="13" viewBox="0 0 13 13"><polyline points="1.5,7 5,10.5 11.5,2.5" fill="none" stroke="#d3122a" stroke-width="2.4"/></svg>Learn what to do first!</li>
      <li><svg width="13" height="13" viewBox="0 0 13 13"><polyline points="1.5,7 5,10.5 11.5,2.5" fill="none" stroke="#d3122a" stroke-width="2.4"/></svg>Stop spending into failing traditional security</li>
      <li><svg width="13" height="13" viewBox="0 0 13 13"><polyline points="1.5,7 5,10.5 11.5,2.5" fill="none" stroke="#d3122a" stroke-width="2.4"/></svg>Shift to a real and automated security</li>
      <li><svg width="13" height="13" viewBox="0 0 13 13"><polyline points="1.5,7 5,10.5 11.5,2.5" fill="none" stroke="#d3122a" stroke-width="2.4"/></svg>Win against global, professional and well funded criminals</li>
    </ul>
  </div>
  <div class="featured-visual" role="img" aria-label="Tablet showing a cybersecurity screen"></div>
  <a href="#" class="btn-contact">CONTACT US FOR A FREE PRESENTATION</a>
</section>

<section class="columns">
  <div class="column">
    <h2 class="column-bar">IMPLEMENT THE TOP-4 CYBER CONTROLS</h2>
    <div class="column-body">
      <p class="body-text">Top International cybersecurity experts and organisations (including the Norvane Department of Homeland Security, The Castrel Department of Defense and the Corven critical security controls) have stated that most companies can best defend against cyberattacks by implementing the following top 4 controls:</p>
      <ul class="tick-list">
        <li><svg width="13" height="13" viewBox="0 0 13 13"><polyline points="1.5,7 5,10.5 11.5,2.5" fill="none" stroke="#d3122a" stroke-width="2.4"/></svg>Application whitelisting</li>
        <li><svg width="13" height="13" viewBox="0 0 13 13"><polyline points="1.5,7 5,10.5 11.5,2.5" fill="none" stroke="#d3122a" stroke-width="2.4"/></svg>Patch &amp; update Applications</li>
        <li><svg width="13" height="13" viewBox="0 0 13 13"><polyline points="1.5,7 5,10.5 11.5,2.5" fill="none" stroke="#d3122a" stroke-width="2.4"/></svg>Patch &amp; update Operating systems</li>
        <li><svg width="13" height="13" viewBox="0 0 13 13"><polyline points="1.5,7 5,10.5 11.5,2.5" fill="none" stroke="#d3122a" stroke-width="2.4"/></svg>Minimize administrator privileges</li>
      </ul>
    </div>
  </div>
  <div class="column">
    <h2 class="column-bar">LATEST UPDATES</h2>
    <div class="column-body">
      <p class="update"><strong>Velmar Cyber Security</strong> One key take-away from the Ostmere International Cyber Security Event: Belgium urgently needs a ONE national cyberstrategy and work from there with other EU members.</p>
      <p class="update"><strong>Velmar Cyber Security</strong> One key take-away from the Ostmere International Cyber Security Event: Belgium urgently needs a ONE national cyberstrategy and work from there with other EU members.</p>
      <p class="update"><strong>Velmar Cyber Security</strong> One key take-away from the Ostmere International Cyber Security Event: Belgium urgently needs a ONE national cyberstrategy and work from there with other EU members.</p>
    </div>
  </div>
</section>

<footer class="site-footer">
  <nav class="footer-nav"><a href="#">HOME</a><a href="#">ABOUT</a><a href="#">SERVICES</a><a href="#">CAREER</a><a href="#">CONTACT</a></nav>
  <div class="social"><span></span><span></span><span></span></div>
</footer>

</body>
</html>
```